Sarood Tradeline Web Design

We need Simple but very Elegant Website for Our Middle East Company based in Kuwait, We are not good in describing design but we need simple but elegant and responsive to attract new market and to enable us competing in business

Industry/Entity Type

It Company

```html
<!DOCTYPE html>
<html lang="en">
<head>
<meta charset="utf-8">
<title>Sarood Tradeline — Landing Page</title>
<link href="https://fonts.googleapis.com/css2?family=Arimo:wght@400;700&display=swap" rel="stylesheet">
<style>
:root{
  --canvas:#f1f1f1;
  --page:#fafafa;
  --ink:#333333;
  --muted:#8a8a8a;
  --accent:#c0492a;
  --rule:#dddddd;
  --footer:#222222;
  --footer-bar:#2e2e2e;
  --footer-text:#bdbdbd;
  --white:#ffffff;
}
*{box-sizing:border-box;margin:0;padding:0}
html,body{width:1200px;height:1200px;overflow:hidden;background:var(--canvas);font-family:"Arimo",Arial,sans-serif}
.page{position:absolute;left:22px;top:0;width:1112px;height:1155px;transform:scale(1.039);transform-origin:0 0;background:var(--page);overflow:hidden}
.abs{position:absolute}

/* testimonials */
.section-title{position:absolute;left:0;width:100%;text-align:center;font-weight:700;font-size:26px;letter-spacing:1.2px;color:var(--ink)}
.title-rule{left:408px;top:112px;width:292px;height:1px;background:var(--rule)}
.title-dot{left:550px;top:108px;width:8px;height:8px;border:1px solid var(--rule);border-radius:50%;background:var(--page)}
.v-dash{left:553px;top:148px;height:262px;border-left:1px dashed var(--rule)}
.h-dash{left:98px;top:299px;width:912px;border-top:1px dashed var(--rule)}
.avatar{width:70px;height:70px;border-radius:50%;background:radial-gradient(circle at 50% 40%,#c9b4a6,#7d6a60)}
.quote{position:absolute;font-size:11px;line-height:18.5px;color:var(--muted)}
.quote p{margin-bottom:9px}
.quote .name{font-weight:700;color:var(--ink);line-height:14px}
.quote .role{line-height:14px}
.quote .role span{color:var(--accent)}

/* help */
.help{left:0;top:501px;width:1112px;height:350px;background:
  radial-gradient(ellipse at 35% 40%,rgba(255,255,255,.85),transparent 45%),
  radial-gradient(ellipse at 75% 50%,#3c4650,transparent 40%),
  linear-gradient(180deg,#8a8078 0%,#c9c6c2 45%,#6d6a66 100%)}
.help-title{top:42px;color:var(--white)}
.help-sub{top:83px;width:100%;text-align:center;font-size:11px;color:#eeeeee}
.card{position:absolute;top:153px;height:163px;background:var(--white);border:1px solid #e2e2e2;text-align:center}
.card-icon{position:absolute;left:50%;top:-23px;margin-left:-23.5px;width:47px;height:47px;border-radius:50%;background:var(--accent);display:flex;align-items:center;justify-content:center}
.card h3{margin-top:40px;font-size:14.5px;letter-spacing:1.3px;color:var(--ink)}
.card p{margin:16px 18px 0;font-size:11px;line-height:18.5px;color:#777}
.card a{display:block;font-size:11px;line-height:18.5px;color:var(--accent);text-decoration:none}

/* footer */
.footer{left:0;top:851px;width:1112px;height:254px;background:var(--footer)}
.follow{left:455px;top:43px;width:200px;text-align:center;font-size:12.5px;color:var(--footer-text);letter-spacing:.3px}
.socials{left:470px;top:69px;width:170px;display:flex;justify-content:center;gap:14px}
.socials span{width:17px;height:17px;border-radius:50%;background:#e8e8e8}
.hours{left:821px;top:42px;width:210px;font-size:11px;line-height:18.5px;color:#d0d0d0}
.hours h4{font-size:12.5px;letter-spacing:1px;color:#9a9a9a;margin-bottom:8px}
.hours p{margin-bottom:9px}
.hours b{color:var(--white)}
.bar{left:0;top:1105px;width:1112px;height:46px;background:var(--footer-bar);border-top:1px solid #3a3a3a}
.copy{left:93px;top:18px;font-size:10px;color:#cfcfcf}
.nav{right:40px;top:16px;display:flex;gap:22px;font-size:11px;font-weight:700;color:#cfcfcf}
.nav span:nth-child(6){margin-left:8px}
.nav span:nth-child(7){margin-left:8px}
</style>
</head>
<body>
<div class="page">

  <section class="testimonials">
    <h2 class="section-title" style="top:49px">WHAT OTHERS SAY ABOUT US</h2>
    <div class="abs title-rule"></div>
    <div class="abs title-dot"></div>
    <div class="abs v-dash"></div>
    <div class="abs h-dash"></div>

    <div class="abs avatar" style="left:98px;top:166px" role="img" aria-label="Portrait photo of Lina R. Haddad"></div>
    <div class="quote" style="left:187px;top:166px;width:355px">
      <p>Nulla consequat massa quis enim. Donec pede justo, fringilla vel, aliquet nec, vulputate eget, arcu. In enim justo, rhoncus ut, imperdiet a, venenatis vitae, justo. Nullam dictum felis eu pede mollis pretium. Integer tincidunt. Cras dapibus.</p>
      <div class="name">Lina R. Haddad</div>
      <div class="role">Marketing – <span>TripLedger</span></div>
    </div>

    <div class="abs avatar" style="left:571px;top:166px" role="img" aria-label="Portrait photo of Nora Qasim"></div>
    <div class="quote" style="left:660px;top:166px;width:350px">
      <p>In enim justo, rhoncus ut, imperdiet a, venenatis vitae, justo. Nullam dictum felis eu pede mollis pretium. Integer tincidunt. Cras dapibus.</p>
      <div class="name">Nora Qasim</div>
      <div class="role">CEO – <span>Pressline Hub</span></div>
    </div>

    <div class="abs avatar" style="left:98px;top:317px" role="img" aria-label="Portrait photo of Tarek Bassam"></div>
    <div class="quote" style="left:187px;top:317px;width:350px">
      <p>Nulla consequat massa quis enim. Donec pede justo, fringilla vel, aliquet nec, vulputate eget, arcu.</p>
      <div class="name">Tarek Bassam</div>
      <div class="role">Public Relations – <span>Gulfwave Telecom</span></div>
    </div>

    <div class="abs avatar" style="left:571px;top:317px" role="img" aria-label="Portrait photo of Dr. Sami Fares"></div>
    <div class="quote" style="left:660px;top:317px;width:350px">
      <p>In enim justo, rhoncus ut, imperdiet a, venenatis vitae, justo. Nullam dictum felis eu pede mollis pretium. Integer tincidunt. Cras dapibus.</p>
      <div class="name">Dr. Sami Fares</div>
      <div class="role">Dean of Medicine – <span>Medora Labs</span></div>
    </div>
  </section>

  <section class="abs help" role="img" aria-label="Blurred office background photo">
    <h2 class="section-title help-title">IN CASE YOU NEED HELP</h2>
    <div class="abs help-sub">There are several ways to contact us</div>

    <div class="card" style="left:97px;width:269px">
      <div class="card-icon"><svg width="20" height="20" viewBox="0 0 20 20"><text x="10" y="16" text-anchor="middle" font-family="Arimo,Arial,sans-serif" font-weight="700" font-size="18" fill="#fff">?</text></svg></div>
      <h3>PRESALES QUESTION?</h3>
      <p>Lorem ipsum dolor sit amet, consectetuer adipiscing elit. Aenean commodo ligula eget dolor. Aenean massa.</p>
      <a href="#">Learn more</a>
    </div>
    <div class="card" style="left:420px;width:267px">
      <div class="card-icon"><svg width="18" height="18" viewBox="0 0 18 18" fill="none" stroke="#fff" stroke-width="1.8"><circle cx="9" cy="9" r="7"/><circle cx="9" cy="9" r="3"/><path d="M4 4l3 3M14 4l-3 3M4 14l3-3M14 14l-3-3"/></svg></div>
      <h3>NEED SUPPORT?</h3>
      <p>Donec quam felis, ultricies nec, pellentesque eu, pretium quis, sem. Nulla consequat massa quis enim.</p>
      <a href="#">Learn more</a>
    </div>
    <div class="card" style="left:742px;width:267px">
      <div class="card-icon"><svg width="16" height="16" viewBox="0 0 16 16" fill="none" stroke="#fff" stroke-width="1.5"><rect x="2" y="1.5" width="12" height="13"/><path d="M5 5h6M5 8h6M5 11h6"/></svg></div>
      <h3>CHECK FORUM</h3>
      <p>Donec pede justo, fringilla vel, aliquet nec, vulputate eget, arcu. In enim juserdiet a, venenatis vitae, justo.</p>
      <a href="#">Learn more</a>
    </div>
  </section>

  <footer class="abs footer">
    <div class="abs follow">FOLLOW US</div>
    <div class="abs socials"><span></span><span></span><span></span><span></span><span></span><span></span></div>
    <div class="abs hours">
      <h4>BUSINESS HOURS</h4>
      <p>Our support Hotline is available 24 Hours a day: (555) 210 987 6543</p>
      <div><b>Monday-Friday:</b> 9am to 5pm</div>
      <div><b>Saturday:</b> 10am to 2pm</div>
      <div><b>Sunday:</b> Closed</div>
    </div>
  </footer>

  <div class="abs bar">
    <div class="abs copy">© Copyright -</div>
    <nav class="abs nav"><span>Home</span><span>About us</span><span>Products</span><span>Industries</span><span>Innovation</span><span>Careers</span><span>News &amp; Media</span></nav>
  </div>
</div>
</body>
</html>
```